University Entrepreneurship Housing Cohort Needs a Flyer Design

Wrenfield College's Venture and Discovery Center needs a flyer designed for their new "V-Nest" (short for Venture Nest) Living Learning Community.

The purpose of the V-Nest Residential Cohort (RC) is to provide students at Wrenfield College with the opportunity to live, learn, and participate in activities that have an Venture and Discovery Center focus. Students with entrepreneurial ambitions will be able to connect with others who share those similar interests and aspirations. The community will create a space for students to learn about entrepreneurial and innovative ways of thinking and working, and to begin to implement their ideas using RC provided resources (e.g,, workshops, site visits, mentors, and peer-networking). The RC will also include an on-site V-Nest Commons, which functions as a study space for V-Nest students. The lounge will have dry-erase walls, a 65-inch touch screen monitor, internet connectivity, and printing capabilities. The final design should communicate an exciting and innovative focused opportunity for young college students.

Note: Both logos need to be on the flyer, but pictures can be selected additionally as desired.

Target Market(s)

Undergraduate students who plan to live in on campus housing and have an interest in Venture and Discovery Center

Industry/Entity Type

University

Font styles to use
Sans Serif

Requirements
Must have
• Both logos need to be on the flyer, but pictures can be selected additionally as desired.
• Font: Gill Sans (for larger text) and Usherwood (for smaller text)
• The purpose of the Venture Nest (V-Nest) Living Learning Community (RC) is to provide students at Wrenfield College with the opportunity to live, learn, and participate in activities that have an Venture and Discovery Center focus.
• Students with entrepreneurial ambitions will be able to connect with others who share similar interests and aspirations. Using resources provided by the V-Nest RC and the Venture and Discovery Center, residents will begin to develop their ideas, as well as participate in experiences that include workshops, competitions, mentorship, exposure to the Atlanta ecosystem, and peer-to-peer networking.
• The V-Nest Commons will include:
• - Collaborative study space
• - Dry-erase walls
• - 65-inch touchscreen monitor
• - Internet connectivity
• - Printing capabilities
• Website: vdc.wrenfield-example.edu
• Phone: 555-208-3164
• Twitter: @WCVDCtr
• Facebook: WC_VDCtr
• LinkedIn: Venture & Discovery Center at Wrenfield College
Nice to have
• Color codes:
• Blue PMS 286
• RED PMS 186
• Grey PMS 404
• More details here: http://brandpack.wrenfield-example.edu/guidelines/visual-identity/type-color-usage/

```html
<!DOCTYPE html>
<html lang="en">
<head>
<meta charset="utf-8">
<title>V-Nest Residential Cohort Flyer</title>
<link rel="stylesheet" href="https://fonts.googleapis.com/css2?family=Open+Sans:wght@400;600;700&family=Merriweather:wght@300&display=swap">
<style>
  :root {
    --brand-blue: #3049a2;
    --deep-blue: #1f3b9b;
    --overlay-blue: rgba(40, 66, 170, 0.72);
    --paper: #f3f3f3;
    --text-grey: #5a5a5a;
    --bullet-grey: #555;
    --white: #ffffff;
  }
  * { margin: 0; padding: 0; box-sizing: border-box; }
  html, body { width: 939px; height: 1200px; overflow: hidden; background: var(--paper); }
  .flyer {
    position: relative; width: 939px; height: 1200px; overflow: hidden;
    background: var(--paper);
    font-family: "Open Sans", Arial, sans-serif;
    color: var(--text-grey);
  }
  .hero-photo {
    position: absolute; left: 0; top: 0; width: 939px; height: 423px;
    background: linear-gradient(135deg, #5a4a3c 0%, #b6a58f 35%, #e8e2d8 65%, #f4f4f6 100%);
  }
  .shapes { position: absolute; left: 0; top: 0; width: 939px; height: 1200px; }
  .brand-mark {
    position: absolute; left: 58px; top: 496px; width: 200px;
    display: flex; align-items: center; gap: 12px;
    font-weight: 700; font-size: 30px; color: var(--deep-blue);
  }
  .brand-mark .mark-square { width: 34px; height: 34px; background: var(--brand-blue); flex: none; }
  .title-block { position: absolute; right: 97px; top: 440px; text-align: right; color: var(--white); }
  .title { font-size: 88px; font-weight: 400; line-height: 1; letter-spacing: 1px; }
  .subtitle { font-family: "Merriweather", Georgia, serif; font-weight: 300; font-size: 25px; margin-top: 6px; }
  .purpose {
    position: absolute; left: 37px; top: 657px; width: 866px;
    font-size: 22.5px; line-height: 29px; text-align: justify;
  }
  .section-pill {
    position: absolute; left: 0; top: 803px; width: 424px; height: 57px;
    background: var(--deep-blue); border-radius: 0 14px 14px 0;
    color: var(--white); font-weight: 700; font-size: 26px; letter-spacing: 0.5px;
    display: flex; align-items: center; padding-left: 53px;
  }
  .amenities { position: absolute; left: 52px; top: 880px; list-style: none; }
  .amenities li {
    display: flex; align-items: center; gap: 10px;
    font-size: 24px; height: 38px; color: var(--text-grey);
  }
  .amenities svg { width: 22px; height: 22px; flex: none; }
  .gallery-tile { position: absolute; width: 179px; height: 135px; border: 1px solid #ddd; }
  .tile-entrance { left: 530px; top: 808px; background: linear-gradient(160deg, #cfd7e4, #9a6a55 60%, #6d4a3a); }
  .tile-lounge { left: 723px; top: 808px; background: linear-gradient(160deg, #c9d6d2, #8a5040 55%, #3c4e6a); }
  .tile-study { left: 530px; top: 958px; background: linear-gradient(160deg, #e7dfd2, #c98b7a 55%, #c9303f); }
  .tile-window { left: 723px; top: 958px; background: linear-gradient(160deg, #a9b8c8, #6d7c8a 55%, #3b4a60); }
  .college-mark { position: absolute; left: 35px; top: 1110px; display: flex; align-items: center; gap: 10px; }
  .college-mark .mark-square { width: 24px; height: 24px; background: var(--deep-blue); flex: none; }
  .college-name { font-size: 25px; font-weight: 400; color: var(--text-grey); line-height: 27px; }
  .college-divider { width: 1px; height: 50px; background: var(--text-grey); margin: 0 4px; }
  .center-name { font-size: 16px; font-weight: 400; color: var(--text-grey); line-height: 23px; letter-spacing: 0.5px; text-transform: uppercase; white-space: nowrap; }
  .contact-bar {
    position: absolute; top: 1125px; height: 75px; right: 28px; left: 470px;
    display: flex; align-items: center; justify-content: flex-end; gap: 22px; color: var(--white); font-size: 23px;
  }
  .contact-item { display: flex; align-items: center; gap: 8px; white-space: nowrap; }
  .contact-item svg { width: 22px; height: 22px; flex: none; }
  .contact-web { font-size: 18px; }
</style>
</head>
<body>
<main class="flyer">
  <div class="hero-photo" role="img" aria-label="Photo of two students on a dorm bed looking at a laptop together"></div>

  <svg class="shapes" viewBox="0 0 939 1200" aria-hidden="true">
    <polygon points="0,226 356,423 0,423" fill="var(--overlay-blue)"/>
    <polygon points="245,423 939,423 939,592 356,592" fill="var(--brand-blue)"/>
    <polygon points="462,1125 939,1125 939,1200 417,1200" fill="var(--brand-blue)"/>
  </svg>

  <div class="brand-mark"><span class="mark-square"></span><span>V-Nest</span></div>

  <header class="title-block">
    <h1 class="title">V-Nest</h1>
    <p class="subtitle">Residential Cohort</p>
  </header>

  <p class="purpose">The purpose of the V-Nest Residential Cohort (RC) is to provide undergraduate students at Wrenfield College with the opportunity to live, learn, and participate in activities that have an entrepreneurship and innovation focus.</p>

  <h2 class="section-pill">THE LOUNGE WILL HAVE</h2>
  <ul class="amenities">
    <li><svg viewBox="0 0 22 22"><circle cx="11" cy="11" r="10" fill="var(--bullet-grey)"/><polygon points="8,6 16,11 8,16" fill="var(--white)"/></svg>Dry-erase walls</li>
    <li><svg viewBox="0 0 22 22"><circle cx="11" cy="11" r="10" fill="var(--bullet-grey)"/><polygon points="8,6 16,11 8,16" fill="var(--white)"/></svg>65-inch touch screen monitor</li>
    <li><svg viewBox="0 0 22 22"><circle cx="11" cy="11" r="10" fill="var(--bullet-grey)"/><polygon points="8,6 16,11 8,16" fill="var(--white)"/></svg>Internet connectivity</li>
    <li><svg viewBox="0 0 22 22"><circle cx="11" cy="11" r="10" fill="var(--bullet-grey)"/><polygon points="8,6 16,11 8,16" fill="var(--white)"/></svg>Printing capabilities</li>
  </ul>

  <div class="gallery-tile tile-entrance" role="img" aria-label="Photo of the residence hall entrance and commons sign"></div>
  <div class="gallery-tile tile-lounge" role="img" aria-label="Photo of students working together on a lounge sofa"></div>
  <div class="gallery-tile tile-study" role="img" aria-label="Photo of two students talking in a dorm room"></div>
  <div class="gallery-tile tile-window" role="img" aria-label="Photo of a student studying by a window with a city view"></div>

  <div class="college-mark">
    <span class="mark-square"></span>
    <span class="college-name">Wrenfield<br>College</span>
    <span class="college-divider"></span>
    <span class="center-name">Venture and<br>Discovery Center</span>
  </div>

  <footer class="contact-bar">
    <span class="contact-item">
      <svg viewBox="0 0 24 24"><circle cx="12" cy="12" r="10.5" fill="none" stroke="var(--white)" stroke-width="2"/><path d="M8.5 6.5l2 2-1.2 1.6c.7 1.6 1.9 2.8 3.5 3.5l1.6-1.2 2 2-1.3 1.8c-3.6-.3-7.1-3.8-7.4-7.4z" fill="var(--white)"/></svg>
      555-208-3164
    </span>
    <span class="contact-item contact-web">
      <svg viewBox="0 0 24 24"><circle cx="12" cy="12" r="10" fill="none" stroke="var(--white)" stroke-width="2"/><ellipse cx="12" cy="12" rx="4" ry="10" fill="none" stroke="var(--white)" stroke-width="1.6"/><line x1="2" y1="12" x2="22" y2="12" stroke="var(--white)" stroke-width="1.6"/></svg>
      vdc.wrenfield-example.edu
    </span>
  </footer>
</main>
</body>
</html>
```